Interior Decoration and Concept Store needs a webpage design

Sophisticated website for my business, name Wren Hollow. Wren Hollow is a design service and homewares store run by interior decorator Marion Tulk.

Marion's qualification and work experience as an interior decorator, is able to provide advice and recommendations for interior and exterior concepts, colour consultations, furniture, lighting, decor concepts and products are sourced for individual projects. A re-upholstery service is also provided.

Gatherly icon.
Projects page.
Profile page.
Established 2009
Medial page

Industry/Entity Type

Store

```html
<!DOCTYPE html>
<html lang="en">
<head>
<meta charset="utf-8">
<title>Contact Us – Wren Hollow</title>
<link rel="stylesheet" href="https://fonts.googleapis.com/css2?family=Arimo:ital,wght@0,400;0,700;1,400&family=Cormorant+Garamond:wght@300&display=swap">
<style>
  :root {
    --ink: #1e1e1e;
    --muted: #6b6b6b;
    --rule: #9a9a9a;
    --field-border: #b9b9b9;
    --frame: #ececec;
    --button: #b3b3b3;
    --icon: #c9c9c9;
    --paper: #ffffff;
    --hero-a: #cfcabc;
    --hero-b: #8d8479;
    --hero-c: #e7e3da;
    --map: #e8e4dc;
  }
  * { box-sizing: border-box; margin: 0; padding: 0; }
  html, body { width: 1200px; height: 901px; overflow: hidden; background: var(--paper); }
  body { font-family: "Arimo", Arial, sans-serif; color: var(--ink); letter-spacing: 0.04em; position: relative; }

  .page-frame { position: absolute; left: 111px; top: 0; width: 977px; height: 901px;
    border-left: 1px solid var(--frame); border-right: 1px solid var(--frame); }

  .brand { position: absolute; left: 116px; top: 34px; font-size: 30px; color: #4a4a4a;
    letter-spacing: 0.06em; display: flex; align-items: center; gap: 10px; }
  .brand .dot { width: 14px; height: 14px; border-radius: 50%; background: #8a8a8a; }

  .main-nav { position: absolute; top: 51px; left: 0; width: 1200px; font-size: 15px; letter-spacing: 0.06em; }
  .main-nav a { position: absolute; color: var(--ink); text-decoration: none; }
  .main-nav a.current::after { content: ""; position: absolute; left: 0; right: 0; top: 20px; height: 4px; background: var(--button); }

  .rule { position: absolute; left: 111px; width: 977px; height: 1px; background: var(--rule); }

  .hero { position: absolute; left: 111px; top: 114px; width: 976px; height: 174px;
    background: linear-gradient(90deg, var(--hero-c) 0%, var(--hero-a) 25%, var(--hero-b) 55%, var(--hero-a) 80%, var(--hero-c) 100%); }
  .hero-title { position: absolute; left: 111px; top: 244px; font-family: "Cormorant Garamond", Georgia, serif;
    font-weight: 300; font-size: 54px; line-height: 48px; color: var(--paper); letter-spacing: 0.01em; }

  .details { position: absolute; left: 111px; top: 318px; font-size: 13px; line-height: 18px; }
  .details dt { font-weight: 700; }
  .details dd { margin-bottom: 19px; }
  .intro { position: absolute; left: 111px; top: 483px; width: 600px; font-size: 13px; line-height: 19px; font-style: italic; }

  .enquiry label.field-label { position: absolute; left: 111px; font-size: 13px; }
  .enquiry .field { position: absolute; left: 111px; width: 598px; height: 23px; border: 1px solid var(--field-border); background: var(--paper); }
  .enquiry .message { height: 79px; }
  .send { position: absolute; left: 111px; top: 815px; width: 55px; height: 29px; background: var(--button);
    color: var(--paper); font-size: 13px; border: 0; letter-spacing: 0.06em; font-family: inherit; }
  .copy-option { position: absolute; left: 358px; top: 821px; font-size: 13px; display: flex; align-items: center; gap: 9px; }
  .copy-option .box { width: 17px; height: 17px; border: 1px solid var(--field-border); }

  .map { position: absolute; left: 762px; top: 321px; width: 326px; height: 325px; background: var(--map); border: 1px solid #d2cdc3; }

  .social { position: absolute; left: 762px; top: 715px; list-style: none; font-size: 13px; font-style: italic; color: var(--muted); }
  .social li { display: flex; align-items: center; gap: 14px; height: 23px; margin-bottom: 12px; }
  .social .tile { width: 23px; height: 23px; background: var(--icon); }

  .site-footer { position: absolute; left: 111px; top: 860px; font-size: 11px; line-height: 15px; }
  .site-footer b { margin-right: 4px; }
  .site-footer span { margin-right: 16px; }
  .site-footer small { font-size: 11px; font-style: italic; display: block; }
  .footer-icons { position: absolute; left: 1005px; top: 864px; display: flex; gap: 6px; }
  .footer-icons i { width: 23px; height: 23px; background: var(--icon); display: block; }
</style>
</head>
<body>
  <div class="page-frame"></div>

  <div class="brand"><span class="dot"></span>Wren Hollow</div>

  <nav class="main-nav">
    <a class="current" style="left:580px">HOME</a>
    <a style="left:668px">ABOUT US</a>
    <a style="left:786px">PROJECTS</a>
    <a style="left:907px">MEDIA</a>
    <a style="left:998px">CONTACT US</a>
  </nav>

  <div class="rule" style="top:107px"></div>

  <div class="hero" role="img" aria-label="Photograph of a timber sideboard with amber glass bowls on a sunlit verandah"></div>
  <h1 class="hero-title">CONTACT US</h1>

  <div class="rule" style="top:296px"></div>

  <dl class="details">
    <dt>ADDRESS</dt><dd>4/27 Alder Lane Arcade, Alder Lane, Harwood East 3290</dd>
    <dt>EMAIL</dt><dd>info@wrenhollow.com.au</dd>
    <dt>TELEPHONE</dt><dd>03 5417 2086</dd>
  </dl>

  <p class="intro">Please complete the below form and we will have one of our friendly professionals return your enquiry as soon as possible.</p>

  <form class="enquiry">
    <label class="field-label" style="top:540px">Enter your Name</label>
    <div class="field" style="top:564px"></div>
    <label class="field-label" style="top:595px">E-mail address</label>
    <div class="field" style="top:619px"></div>
    <label class="field-label" style="top:650px">Contact Phone Number</label>
    <div class="field" style="top:674px"></div>
    <label class="field-label" style="top:706px">Enter your Message</label>
    <div class="field message" style="top:730px"></div>
    <button class="send" type="button">SEND</button>
    <div class="copy-option"><span class="box"></span>E-mail a copy of this message to your own address</div>
  </form>

  <div class="map" role="img" aria-label="Street map showing the store location"></div>

  <ul class="social">
    <li><span class="tile"></span>Find us on Gatherly</li>
    <li><span class="tile"></span>Follow us on Chirper</li>
    <li><span class="tile"></span>Snapfolio</li>
  </ul>

  <div class="rule" style="top:850px"></div>

  <footer class="site-footer">
    <b>Tel</b><span>03 5417 2086</span><b>Email</b><span>info@wrenhollow.com.au</span><b>Address</b>4/27 Alder Lane Arcade, Alder Lane, Harwood East 3290
    <small>Copyright Wren Hollow 2014</small>
  </footer>
  <div class="footer-icons"><i></i><i></i><i></i></div>
</body>
</html>
```